Fresh and Modern Real Estate Land Website

This Real Estate Agent sells only land.
The wordpress design will need to work well with responsive Avada theme.
Colors should complement the attached Home-Header.jpg, the Sonoran Desert, Southwest Region of Arizona and Tucson.
Home page layout to include
- Logo Attached: NewLogo.png
- Agent Photo: AdaMorton.jpg
- Contact Detials: use Phone
- Slogan: "I've Never Shown a House"
- Static header or Main image (see Attached Home-Header.jpg) - The dimensions of this shot may not be correct for your design. Please select from similar stock if needed and provide stock photo id.
- Intro/Welcome Text See Attached: Intro.txt
- Vertical or Horizontal display of "New" listings (include: Photo, Price, exerpt/intro) see: Properties.zip
- Tools of the trade. Home page will have a section called "Tools Of the Trade" These are items the agent uses in her work. This seciton will need to be 3 or More Images about 100 characters of text and Title. These will rotate through about 12 different tools. see: tools-of-the-trade.zip
Footer to include Contact Info/Recent Blog Posts/Testimonial
No Social Network icons
Main Menu:
Home
Properties
Testimonials
Services
About Ada
Blog
Contact
Real Estate
- Marck Script google/Times new Roman is logo. Designers Choice.

```html
<!DOCTYPE html>
<html lang="en">
<head>
<meta charset="utf-8">
<title>Ada Morton – Tucson Land</title>
<link href="https://fonts.googleapis.com/css2?family=Ubuntu:wght@400;500;700&family=Noto+Serif:ital,wght@1,400;1,700&display=swap" rel="stylesheet">
<style>
:root{
  --orange:#f47b20;
  --orange-dark:#d9600e;
  --ink:#3a3a3a;
  --muted:#666;
  --paper:#f1f0ee;
  --white:#ffffff;
  --rule:#cfcfcf;
  --navy:rgba(18,38,58,.88);
  --footer:#1d1d1d;
  --footer-base:#111111;
}
*{margin:0;padding:0;box-sizing:border-box}
html,body{width:1200px;height:2177px;overflow:hidden}
body{font-family:"Ubuntu",sans-serif;color:var(--ink);background:var(--white);position:relative}
.abs{position:absolute}

/* header */
.site-header{position:absolute;left:0;top:0;width:1200px;height:126px;background:var(--paper)}
.brand{left:138px;top:34px;font-size:40px;font-weight:700;color:var(--orange);letter-spacing:.5px}
.call{left:824px;top:44px;display:flex;align-items:center;gap:12px;font-size:19px;color:#444}
.call strong{font-weight:700;margin-left:6px}

/* nav */
.main-nav{position:absolute;left:0;top:126px;width:1200px;height:50px;background:var(--orange)}
.main-nav ul{list-style:none;display:flex;position:absolute;left:238px;top:0;height:50px;align-items:center}
.main-nav li{color:var(--white);font-size:19px;font-weight:500;padding:0 14px;border-left:1px solid rgba(255,255,255,.35);line-height:26px}
.main-nav li:first-child{border-left:none}
.main-nav li.current{position:relative}
.main-nav li.current::before{content:"";position:absolute;left:0;top:-19px;width:64px;height:44px;background:var(--orange-dark);z-index:-1}
.main-nav li.current::after{content:"";position:absolute;left:64px;top:-19px;border-left:9px solid #a9480a;border-bottom:9px solid transparent}
.main-nav li.current{z-index:1}
.main-nav li.current span{position:relative;text-decoration:underline}

/* hero */
.hero{position:absolute;left:0;top:176px;width:1200px;height:410px;
  background:linear-gradient(180deg,#1f7fd0 0%,#4aa0e2 22%,#9a6a48 40%,#7d6a4a 52%,#667a3a 70%,#4c6a2a 100%)}
.hero-quote{left:136px;top:52px;width:408px;height:61px;background:var(--navy);
  clip-path:polygon(0 0,100% 0,94% 100%,0 100%);color:var(--white);font-size:26px;font-weight:500;
  display:flex;align-items:center;padding-left:10px}
.hero-quote .q{font-size:34px;font-family:"Noto Serif",serif;line-height:1;margin:0 8px;position:relative;top:-6px}
.hero-arrow{top:135px}
.dots{left:552px;top:357px;display:flex;gap:9px}
.dots i{display:block;width:15px;height:15px;border-radius:50%;background:#d6d6d6}
.dots i.on{background:var(--orange)}

/* welcome */
.welcome{position:absolute;left:0;top:586px;width:1200px;height:335px;background:var(--paper);text-align:center}
.welcome h2{margin-top:51px;font-size:22px;font-weight:400;color:var(--orange)}
.welcome p{width:820px;margin:22px auto 0;font-size:19.5px;line-height:25px;color:#333}
.welcome p + p{margin-top:25px}
.welcome em{font-style:normal;color:var(--orange)}

/* listings */
.listings{position:absolute;left:0;top:921px;width:1200px;height:324px;background:var(--white)}
.listing{position:absolute;top:44px;width:190px}
.listing .photo{height:106px;border:4px solid #c9c9c9}
.listing .head{display:flex;justify-content:space-between;margin-top:14px;padding-bottom:8px;border-bottom:1px solid #ddd;font-size:14px;color:#222}
.listing .price{color:var(--orange)}
.listing p{margin-top:10px;font-size:10.5px;line-height:15px;color:#555}
.btn{display:inline-block;margin-top:14px;margin-left:3px;width:113px;height:27px;line-height:27px;text-align:center;background:var(--orange);color:var(--white);font-size:13px;font-weight:500;border-radius:2px}

/* about */
.about{position:absolute;left:0;top:1245px;width:1200px;height:311px;background:var(--paper)}
.about .portrait{left:310px;top:41px;width:159px;height:215px;background:linear-gradient(180deg,#3d6fa8 0%,#4f7db0 55%,#c2262a 75%,#c3282b 100%)}
.about h2{left:515px;top:40px;font-size:26px;font-weight:400;color:var(--orange)}
.about .copy{left:514px;top:89px;width:500px;font-size:15.5px;line-height:26px;color:#444}
.about .copy p + p{margin-top:10px}

/* tools */
.tools{position:absolute;left:0;top:1556px;width:1200px;height:330px;background:var(--white)}
.tools .rule{top:39px;height:1px;background:var(--rule)}
.tools h2{left:0;width:1200px;top:22px;text-align:center;font-size:25px;font-weight:400;color:var(--orange)}
.tool{position:absolute;top:94px;width:163px}
.tool .frame{height:141px;border:4px solid #d3d3d3;border-radius:3px;position:relative;overflow:hidden;background:#fff}
.tool .img{position:absolute;left:0;top:0;right:0;height:108px}
.tool .label{position:absolute;left:0;right:0;bottom:0;height:25px;background:#e8e8e8;font-size:15.5px;line-height:25px;padding-left:6px;color:#333}
.tool p{margin-top:15px;font-size:11.5px;line-height:16px;color:#555}

/* footer */
.site-footer{position:absolute;left:0;top:1886px;width:1200px;height:247px;background:var(--footer);color:#ddd}
.fcol{position:absolute;top:58px;width:222px}
.fcol h3{font-size:20px;font-weight:500;color:var(--white);padding-bottom:10px;border-bottom:1px solid #777}
.contact-row{display:flex;align-items:flex-start;gap:18px;font-size:14.5px;line-height:24px;margin-top:14px}
.contact-row svg{flex:none;margin-top:3px}
.post{display:flex;gap:11px;padding:14px 0 9px;border-bottom:1px solid #444}
.post:last-child{border-bottom:none}
.post .thumb{flex:none;width:48px;height:43px;background:linear-gradient(180deg,#7b98b6,#8d7a5a 55%,#5d6b3c)}
.post h4{font-size:11.5px;font-weight:700;color:var(--white)}
.post p{font-size:9px;line-height:11px;color:#ccc;font-weight:700}
.post p b{color:var(--orange)}
.quote{position:relative;margin-top:14px;padding-left:26px;font-family:"Noto Serif",serif;font-style:italic;font-size:13px;line-height:16px;color:#ddd}
.quote .mark{position:absolute;left:0;top:-6px;font-size:34px;color:var(--orange);font-style:normal;font-weight:700}
.quote cite{display:block;text-align:right;margin-top:12px;font-weight:700;font-size:14px;color:#eee;padding-right:6px}
.copyright{position:absolute;left:0;top:2133px;width:1200px;height:44px;background:var(--footer-base);color:#bbb;font-size:11.5px;text-align:center;line-height:44px}
</style>
</head>
<body>

<header class="site-header">
  <div class="abs brand">Ada Morton</div>
  <div class="abs call">
    <svg width="32" height="32" viewBox="0 0 32 32" aria-hidden="true"><circle cx="16" cy="16" r="14" fill="none" stroke="#222" stroke-width="2.5"/><path d="M11 9c1-1 2-1 3 0l1.5 2.5c.5 1 0 2-.8 2.5-.5.3-.5 1 0 2l1.5 1.8c.8.9 1.5 1 2 .4.7-.8 1.7-1.1 2.5-.5L23 19.4c1 .8.8 2-.2 2.8-2.3 1.9-6 .3-9-3.4-3-3.6-4.2-7.7-2.8-9.8z" fill="#222"/></svg>
    <span>Call Us <strong>012-555-0148</strong></span>
  </div>
</header>

<nav class="main-nav">
  <ul>
    <li class="current"><span>Home</span></li>
    <li>Properties</li>
    <li>Testimonials</li>
    <li>Services</li>
    <li>About Ada</li>
    <li>Blog</li>
    <li>Contact</li>
  </ul>
</nav>

<section class="hero" role="img" aria-label="Sonoran desert landscape with saguaro cacti below rocky mountains and blue sky">
  <div class="abs hero-quote"><span class="q">“</span>I've Never Shown a House<span class="q">”</span></div>
  <svg class="abs hero-arrow" style="left:136px" width="24" height="42" viewBox="0 0 24 42" aria-hidden="true"><path d="M20 4L4 21l16 17" fill="none" stroke="#fff" stroke-width="3"/></svg>
  <svg class="abs hero-arrow" style="left:1038px" width="24" height="42" viewBox="0 0 24 42" aria-hidden="true"><path d="M4 4l16 17L4 38" fill="none" stroke="#fff" stroke-width="3"/></svg>
  <div class="abs dots"><i></i><i class="on"></i><i></i><i></i></div>
</section>

<section class="welcome">
  <h2>Welcome to the Land Lady</h2>
  <p>When you are looking for Tucson land, <em>Ada Morton</em>'s experience has "landed" her among the top 1/2% ranking of all Realtors, and that's just selling LAND!</p>
  <p>Ada is proud to say that she STILL has never sold a house... but she does know the best who do.&nbsp; 90% of real estate is sold by 10% of the Realtors and, during nearly 30 years of selling, Ada knows and is good friends with these 10%. Utilize Ada's contacts so she can match up the right home agent...for YOU!</p>
</section>

<section class="listings">
  <article class="listing" style="left:218px">
    <div class="photo" role="img" aria-label="Desert lot with green brush and distant hills" style="background:linear-gradient(180deg,#9fb9d2 0%,#a7a48a 35%,#6f8a4a 60%,#5a6e3a 100%)"></div>
    <div class="head"><span>Lorem Ipsum</span><span class="price">$120,000</span></div>
    <p>Dummy text only sit amet, consectetur adipisicing elit, sed do eiusmod tempor incididunt ut labore et dolore magna.</p>
    <span class="btn">Read More</span>
  </article>
  <article class="listing" style="left:484px">
    <div class="photo" role="img" aria-label="Golden desert sunset sky" style="background:linear-gradient(180deg,#c86a10 0%,#f2a72a 45%,#e08a18 70%,#6a3a0a 100%)"></div>
    <div class="head"><span>Dolorul maoi</span><span class="price">$120,000</span></div>
    <p>Dummy text only sit amet, consectetur adipisicing elit, sed do eiusmod tempor incididunt ut labore et dolore magna.</p>
    <span class="btn">Read More</span>
  </article>
  <article class="listing" style="left:752px">
    <div class="photo" role="img" aria-label="Saguaro cacti on desert land below mountains" style="background:linear-gradient(180deg,#8fb4d8 0%,#a9b8c4 30%,#8a8c6a 50%,#6b7a45 100%)"></div>
    <div class="head"><span>Put title here</span><span class="price">$120,000</span></div>
    <p>Dummy text only sit amet, consectetur adipisicing elit, sed do eiusmod tempor incididunt ut labore et dolore magna.</p>
    <span class="btn">Read More</span>
  </article>
</section>

<section class="about">
  <div class="abs portrait" role="img" aria-label="Portrait photo of Ada Morton"></div>
  <h2 class="abs">About Ada Morton</h2>
  <div class="abs copy">
    <p>Lorem ipsum dolor sit amet, consectetur adipisicing elit, sed do eius mod tempor incididunt ut labore et dolore magna aliqua. Ut enim ad minim veniam.</p>
    <p>Quis nostrud exercitation ullamco laboris nisi ut aliquip ex ea comm odo consequat. Duis aute irure dolor in reprehenderit in voluptate velit esse cillum dolore eu fugiat nulla.</p>
  </div>
</section>

<section class="tools">
  <div class="abs rule" style="left:131px;width:336px"></div>
  <div class="abs rule" style="left:730px;width:338px"></div>
  <h2 class="abs">Tools Of the Trade</h2>
  <svg class="abs" style="left:131px;top:134px" width="33" height="54" viewBox="0 0 33 54" aria-hidden="true"><path d="M33 0v54L0 27z" fill="#d0d0d0"/></svg>
  <svg class="abs" style="left:1032px;top:134px" width="33" height="54" viewBox="0 0 33 54" aria-hidden="true"><path d="M0 0v54l33-27z" fill="#d0d0d0"/></svg>
  <article class="tool" style="left:268px">
    <div class="frame"><div class="img" role="img" aria-label="Compass with leather case" style="background:radial-gradient(circle at 50% 55%,#4a3a30 0%,#6b5444 40%,#efeeec 75%)"></div><div class="label">Title Here</div></div>
    <p>Lorem ipsum dolor sit amet, consectetur adipis.</p>
  </article>
  <article class="tool" style="left:520px">
    <div class="frame"><div class="img" role="img" aria-label="Roll of orange flagging tape" style="background:radial-gradient(circle at 50% 65%,#f0401a 0%,#f26030 30%,#ffffff 65%)"></div><div class="label">Title Here</div></div>
    <p>Lorem ipsum dolor sit amet, consectetur adipis.</p>
  </article>
  <article class="tool" style="left:772px">
    <div class="frame"><div class="img" role="img" aria-label="Yellow measuring tape reel" style="background:radial-gradient(circle at 55% 60%,#e0b81a 0%,#e8c640 30%,#ffffff 65%)"></div><div class="label">Title Here</div></div>
    <p>Lorem ipsum dolor sit amet, consectetur adipis.</p>
  </article>
</section>

<footer class="site-footer">
  <div class="fcol" style="left:160px">
    <h3>Contact Information</h3>
    <div class="contact-row" style="margin-top:18px">
      <svg width="22" height="20" viewBox="0 0 22 20" aria-hidden="true"><path d="M11 1L1 10h3v9h5v-6h4v6h5v-9h3z" fill="#ddd"/></svg>
      <span>014 Sample Address<br>Houston, Texas 77205</span>
    </div>
    <div class="contact-row">
      <svg width="22" height="22" viewBox="0 0 32 32" aria-hidden="true"><circle cx="16" cy="16" r="14" fill="none" stroke="#ddd" stroke-width="2.5"/><path d="M11 9c1-1 2-1 3 0l1.5 2.5c.5 1 0 2-.8 2.5-.5.3-.5 1 0 2l1.5 1.8c.8.9 1.5 1 2 .4.7-.8 1.7-1.1 2.5-.5L23 19.4c1 .8.8 2-.2 2.8-2.3 1.9-6 .3-9-3.4-3-3.6-4.2-7.7-2.8-9.8z" fill="#ddd"/></svg>
      <span>Phone: (012) 555-0148</span>
    </div>
    <div class="contact-row">
      <svg width="22" height="16" viewBox="0 0 22 16" aria-hidden="true"><rect x="0" y="0" width="22" height="16" fill="#ddd"/><path d="M0 0l11 9L22 0" fill="none" stroke="#1d1d1d" stroke-width="1.8"/></svg>
      <span>adamorton@mesaland.com</span>
    </div>
  </div>

  <div class="fcol" style="left:498px">
    <h3>Recent Blog Posts</h3>
    <div class="post">
      <div class="thumb" role="img" aria-label="Desert landscape thumbnail"></div>
      <div><h4>Pollestuinim denil</h4><p>Lorem ipsum dolor sit amet,<br>consectetur adipisicing elit,<br>sed do eius..<b>[Read More]</b></p></div>
    </div>
    <div class="post">
      <div class="thumb" role="img" aria-label="Desert landscape thumbnail"></div>
      <div><h4>Pollestuinim denil</h4><p>Lorem ipsum dolor sit amet,<br>consectetur adipisicing elit,<br>sed do eius..<b>[Read More]</b></p></div>
    </div>
  </div>

  <div class="fcol" style="left:818px">
    <h3>Testimonial</h3>
    <blockquote class="quote">
      <span class="mark">“</span>
      Lorem ipsum dolor sit amet, consectetur adipisicing elit, sed do eiusmod tempor incid idunt ut labore et.
      <cite>~John Doe, New York</cite>
    </blockquote>
  </div>
</footer>

<div class="copyright">Copyright© AdaMorton2014. All Rights Reserved</div>

</body>
</html>
```